Etiketten-Design für Himbeer-Gin
Zielgruppe
GIN
Aufgabenstellung
Wir benötigen ein Etikett für unseren neuen Himbeere GIN, der Name des GINs lautet: KorvalaGIN und soll für folgende Flasche dargestellt werden: https://www.flakoria-beispiel.de/luma-flasche-500ml-schwarz-beschichtet-tqx41-karton-48stk.html
mit dem Etikett https://klebmarken-beispiel.de/anwendungen/fluoreszierende-etiketten/ Himbeerlastiges Design mit bestehendem Logo (WendelGIN) siehe Daten. Bei Fragen stehe ich gerne zur Verfügung!

```html
<!DOCTYPE html>
<html lang="de">
<head>
<meta charset="utf-8">
<title>KorvalaGIN – Etikett</title>
<link rel="stylesheet" href="https://fonts.googleapis.com/css2?family=Marcellus&family=Open+Sans:wght@700&family=Oswald:wght@500;600&display=swap">
<style>
  :root {
    --page: #fdfdfd;
    --berry-deep: #86064a;
    --berry-mid: #c0196e;
    --berry-bright: #e0308a;
    --berry-soft: #dc4b96;
    --berry-edge: #cd4590;
    --silver: #e6e6e6;
    --blush: #eaa6cb;
    --blush-faint: rgba(240, 170, 210, 0.35);
    --ink-metal: #352a2f;
    --white: #ffffff;
  }
  html, body {
    margin: 0;
    width: 1200px;
    height: 1200px;
    overflow: hidden;
    background: var(--page);
  }
  .canvas {
    position: relative;
    width: 1200px;
    height: 1200px;
  }
  .label {
    position: absolute;
    left: 400px;
    top: 266px;
    width: 406px;
    height: 688px;
    border-radius: 28px;
    overflow: hidden;
    background: linear-gradient(90deg, var(--berry-deep) 8%, var(--berry-mid) 36%, var(--berry-bright) 54%, var(--berry-soft) 70%, var(--berry-edge) 100%);
    box-shadow: 10px 14px 18px rgba(0, 0, 0, 0.28);
  }
  .portrait {
    position: absolute;
    left: 158px;
    top: 4px;
    width: 88px;
    height: 119px;
    border-radius: 44px 44px 40px 40px;
    background: linear-gradient(90deg, rgba(140, 20, 80, 0.55), rgba(240, 150, 195, 0.85));
  }
  .portrait--reflect {
    top: 564px;
    opacity: 0.35;
  }
  .est {
    position: absolute;
    top: 72px;
    font-family: "Marcellus", serif;
    font-size: 14px;
    color: var(--blush);
    letter-spacing: 0.5px;
  }
  .est--left { left: 108px; }
  .est--right { left: 268px; }
  .est--reflect { top: 590px; opacity: 0.35; }
  .brand-name {
    position: absolute;
    left: 0;
    width: 100%;
    top: 178px;
    margin: 0;
    text-align: center;
    font-family: "Marcellus", serif;
    font-weight: 400;
    font-size: 58px;
    line-height: 1;
    color: var(--silver);
  }
  .brand-name--reflect {
    top: 470px;
    color: var(--blush-faint);
  }
  .origin {
    position: absolute;
    left: 0;
    width: 100%;
    top: 294px;
    text-align: center;
    font-family: "Marcellus", serif;
    font-size: 25px;
    letter-spacing: 1px;
    color: var(--blush);
  }
  .style {
    position: absolute;
    left: 0;
    width: 100%;
    top: 326px;
    text-align: center;
    font-family: "Open Sans", sans-serif;
    font-weight: 700;
    font-size: 18px;
    color: var(--blush);
    line-height: 1;
  }
  .style--reflect {
    top: 344px;
    transform: scaleY(-1);
    opacity: 0.45;
  }
  .product {
    position: absolute;
    left: 0;
    width: 100%;
    top: 372px;
    text-align: center;
    font-family: "Oswald", sans-serif;
    font-weight: 600;
    font-size: 31px;
    letter-spacing: 5px;
    color: var(--ink-metal);
    text-shadow: 1px 1px 0 rgba(255, 255, 255, 0.35);
  }
  .facts {
    position: absolute;
    top: 650px;
    font-family: "Oswald", sans-serif;
    font-weight: 500;
    font-size: 20px;
    letter-spacing: 1px;
    color: var(--white);
  }
  .facts--volume { left: 70px; }
  .facts--abv { left: 270px; }
</style>
</head>
<body>
<main class="canvas">
  <section class="label">
    <div class="portrait" role="img" aria-label="Porträt des Brennmeisters"></div>
    <span class="est est--left">ESTD.</span>
    <span class="est est--right">2019</span>
    <h1 class="brand-name">WendelGIN</h1>
    <div class="origin">SCHWÄBISCHER</div>
    <div class="style">DRY GIN</div>
    <div class="style style--reflect" aria-hidden="true">DRY GIN</div>
    <div class="product">KORVALA GIN</div>
    <div class="brand-name brand-name--reflect" aria-hidden="true">WendelGIN</div>
    <span class="est est--left est--reflect" aria-hidden="true">ESTD.</span>
    <span class="est est--right est--reflect" aria-hidden="true">2019</span>
    <div class="portrait portrait--reflect" role="img" aria-label="Gespiegeltes Porträt des Brennmeisters"></div>
    <span class="facts facts--volume">500 ml</span>
    <span class="facts facts--abv">40% vol</span>
  </section>
</main>
</body>
</html>
```